Crypto Exchange Comparison Platform

Let’s design a page that lets users compare hundreds of cryptocurrency exchanges. It will help users compare more info than anywhere else so you can find the best crypto exchange for your needs. The goal is to transform complex data into a clean, visually engaging experience.

Key Features to Design:
- Interactive comparison table with ~ 30 columns
- Filters and dropdown menus for easier usability
- Summary boxes for quick-view statistics
- Visual charts and graphs for key metrics
- Web, mobile, and tablet responsive design

Design Goals:
- Clean, modern aesthetic that makes complex data easily digestible
- Interactive elements (eg. Bar and Spider charts) for user engagement
- "Screenshot-friendly" sections for social media and sharing
- Data visualization focus (charts, graphs, metrics)
- Extremely easy to use on mobile
- Designs that use the color green
- A brand that communicates research and trusted information

Deliverables:
- High-fidelity mockup for desktop, tablet, and mobile versions
- Interactive prototype (Figma preferred)
- Style guide (typography, colors, components)

Note: The goal is to create an intuitive, visually engaging tool that helps users compare cryptocurrency exchanges efficiently while maintaining a clean, professional appearance that works well for social media sharing and content creation.
Updates

Low design quality

Industry/Entity Type

FinTech, Crypto, Finance

Number of Pages Required

1 page

Font styles to use
Other font styles liked:
• Inter or something good for a finance/data related website site

Colors
00AB8E
00BBA5
67D7C9
C6EFE9
E9F9F6

Requirements
Must have
• Please refer to the sketch I uploaded

```html
<!DOCTYPE html>
<html lang="en">
<head>
<meta charset="utf-8">
<title>crypto exchange — Compare Crypto Exchanges</title>
<link rel="stylesheet" href="https://fonts.googleapis.com/css2?family=Poppins:wght@400;500;600;700&display=swap">
<style>
:root{
  --green-dark:#00AB8E;
  --green:#00BBA5;
  --green-mid:#67D7C9;
  --green-light:#C6EFE9;
  --green-pale:#E9F9F6;
  --ink:#111;
  --muted:#777;
  --line:#e6e6e6;
  --white:#fff;
}
*{box-sizing:border-box;margin:0;padding:0}
html,body{width:1200px;height:3445px;overflow:hidden}
body{font-family:"Poppins",sans-serif;color:var(--ink);background:var(--white);position:relative}
.abs{position:absolute}

/* hero */
.hero{position:absolute;left:0;top:0;width:1200px;height:495px;background:linear-gradient(180deg,#050505 0%,#1a1a1a 55%,#3a3a3a 100%);overflow:hidden}
.hero-visual{position:absolute;inset:0;background:radial-gradient(ellipse 360px 200px at 700px 380px,rgba(160,160,160,.35),transparent 70%),radial-gradient(circle 140px at 865px 225px,#d9a93a 0%,#a9761f 60%,transparent 100%)}
.logo{position:absolute;left:87px;top:12px;font-size:29px;font-weight:700;color:var(--green-mid);letter-spacing:-.5px}
.nav{position:absolute;right:90px;top:22px;display:flex;gap:32px}
.nav a{color:var(--white);font-size:14.5px;font-weight:600;text-decoration:none}
.hero h1{position:absolute;left:87px;top:150px;color:var(--white);font-size:56px;line-height:60px;font-weight:700}
.hero p{position:absolute;left:87px;top:282px;color:var(--white);font-size:14px;line-height:20px;width:440px}

/* top pick */
.section-title{position:absolute;width:1200px;text-align:center;font-weight:700}
.pick-card{position:absolute;top:616px;width:216px;height:148px;border-radius:6px;text-align:center}
.pick-card .badge{position:absolute;left:68px;top:-43px;width:80px;height:80px;border-radius:50%;border:4px solid var(--white)}
.pick-card .sub{margin-top:48px;font-size:13.5px;font-weight:600;line-height:16px}
.pick-card .name{font-size:17px;font-weight:700;line-height:20px}
.pick-card .cta{margin-top:18px;font-size:13.5px;font-weight:500}
.pick-a{left:250px;background:var(--green-dark);color:var(--white)}
.pick-b{left:493px;background:var(--green-light);color:var(--ink)}
.pick-c{left:735px;background:var(--green-mid);color:var(--white)}

/* tabs & tools */
.tabs{position:absolute;left:89px;top:836px;display:flex;align-items:center}
.tab{height:56px;padding:0 38px;display:flex;align-items:center;font-size:14px;font-weight:500;border-radius:6px}
.tab.active{background:var(--green-mid);color:var(--white);width:102px;justify-content:center;padding:0}
.tab-tools{position:absolute;top:850px;display:flex;gap:12px;left:891px}
.tool{height:35px;border:1px solid var(--line);border-radius:5px;display:flex;align-items:center;gap:8px;padding:0 12px;font-size:13.5px}

/* table */
.ex-table{position:absolute;left:88px;top:907px;width:1023px;border:1px solid #eee;border-collapse:collapse;font-size:11px}
.ex-table th{height:58px;font-size:9px;font-weight:500;text-align:left;border-bottom:1px solid #eee}
.ex-table td{height:58px;border-bottom:1px solid #eee;font-size:11px}
.ex-table tr:last-child td{border-bottom:none}
.coin{display:flex;align-items:center;gap:6px;font-weight:600;font-size:10px}
.coin i{width:16px;height:16px;border-radius:50%;display:inline-block}
.coin span{color:#8aa;font-weight:400}
.bonus{line-height:12px;font-size:10.5px}

/* charts */
.chart-title{position:absolute;top:1444px;font-size:18px;font-weight:600}
.chart-card{position:absolute;top:1481px;width:418px;height:296px;background:var(--white);box-shadow:0 2px 12px rgba(0,0,0,.12);border-radius:4px}

/* stats */
.stat{position:absolute;top:1852px;text-align:center}
.stat .label{font-size:15px;font-weight:500}
.stat .value{font-size:55px;font-weight:700;line-height:70px;margin-top:4px}
.stat-divider{position:absolute;top:1848px;width:1px;height:100px;background:#ddd}

/* compare */
.select{position:absolute;top:2064px;font-size:14px;font-weight:500}
.score-table{position:absolute;left:87px;top:2395px;width:312px;font-size:11px}
.score-head{display:flex;height:22px;font-size:11px;font-weight:500}
.score-row{display:flex;height:38.6px;align-items:center;border-bottom:1px solid #e6e6e6;font-weight:500}

.panel{position:absolute;left:603px;width:470px;background:var(--white);border:1px solid #ececec;border-radius:6px;box-shadow:0 1px 6px rgba(0,0,0,.06)}
.panel h3{font-size:24px;font-weight:700}
.features{top:2107px;height:245px}
.features h3{position:absolute;left:27px;top:10px}
.features .toggle{position:absolute;right:24px;top:12px;font-size:22px}
.feat-list{position:absolute;left:15px;top:54px;width:440px}
.feat-row{height:35px;display:flex;align-items:center;font-size:11px;border:1px solid #f0f0f0}
.feat-row:nth-child(even){background:#fafafa}
.feat-row .k{width:105px;padding-left:16px}
.feat-row .a{width:195px;display:flex;gap:6px;align-items:center}
.feat-row .b{display:flex;gap:10px;align-items:center}
.up{color:var(--green-dark);font-size:8px}
.down{color:#e53935;font-size:8px}
.acc{height:60px;display:flex;align-items:center;justify-content:space-between;padding:0 30px 0 29px}
.acc span{font-size:22px}
.btn-full{position:absolute;left:613px;top:2637px;width:154px;height:56px;background:var(--green-mid);color:var(--white);border-radius:4px;font-size:14px;font-weight:500;display:flex;align-items:center;justify-content:center}

/* faq */
.faq{position:absolute;left:285px;top:2820px;width:629px}
.faq-item{height:32px;border:1px solid #eee;display:flex;align-items:center;justify-content:space-between;padding:0 14px 0 22px;font-size:11px;font-weight:500;margin-bottom:1px}
.faq-item.open{background:var(--green);color:var(--white);border-color:var(--green);border-radius:4px;margin:4px 0}

/* newsletter */
.newsletter{position:absolute;left:0;top:3012px;width:1200px;height:196px;border-top:2px solid var(--green-light);border-bottom:1px solid #ccc}
.newsletter h2{position:absolute;left:95px;top:66px;font-size:22px;line-height:28px;font-weight:600;width:420px}
.newsletter p{position:absolute;left:95px;top:126px;font-size:14px;line-height:19px;width:395px}
.email{position:absolute;left:571px;top:72px;width:403px;height:56px;border:1px solid #e5e5e5;border-radius:4px 0 0 4px;display:flex;align-items:center;padding-left:24px;font-size:14px;color:#999}
.subscribe{position:absolute;left:974px;top:72px;width:143px;height:56px;background:var(--green-mid);color:var(--white);border-radius:0 4px 4px 0;display:flex;align-items:center;justify-content:center;font-size:14px;font-weight:500}

/* footer */
.footer{position:absolute;left:87px;top:3236px;width:1010px;font-size:13.6px;line-height:19.6px}
.footer .copy{margin-bottom:13px}
</style>
</head>
<body>

<header class="hero">
  <div class="hero-visual" role="img" aria-label="Photograph of a gold coin resting on a dark keyboard"></div>
  <div class="logo">crypto exchange</div>
  <nav class="nav"><a>Cryptocurrencies</a><a>PairScope</a><a>Exchanges</a><a>Community</a><a>Products</a></nav>
  <h1>Compare Crypto<br>Exchanges</h1>
  <p>Find the best cryptocurrency exchange with the most detailed and up-to-date comparison tool.</p>
</header>

<h2 class="section-title" style="top:524px;font-size:22px">Top pick</h2>
<div class="pick-card pick-a"><div class="badge" style="background:#f3b82a"></div><div class="sub">crypto exchange</div><div class="name">VELTRIX</div><div class="cta">Compare ›</div></div>
<div class="pick-card pick-b"><div class="badge" style="background:#0b5cff"></div><div class="sub">crypto exchange</div><div class="name">HARBORCOIN</div><div class="cta">Compare ›</div></div>
<div class="pick-card pick-c"><div class="badge" style="background:#55657a"></div><div class="sub">crypto exchange</div><div class="name">TIDEWELL</div><div class="cta">Compare ›</div></div>

<div class="tabs"><div class="tab active">Fees</div><div class="tab">Features</div><div class="tab" style="padding-left:0">Security</div></div>
<div class="tab-tools">
  <div class="tool"><svg width="20" height="18" viewBox="0 0 20 18" fill="none" stroke="#333" stroke-width="1.3"><path d="M1 3h18M1 9h18M1 15h18"/><circle cx="13" cy="3" r="2.2" fill="#fff"/><circle cx="6" cy="9" r="2.2" fill="#fff"/><circle cx="12" cy="15" r="2.2" fill="#fff"/></svg>Filter</div>
  <div class="tool"><svg width="22" height="18" viewBox="0 0 22 18" fill="none" stroke="#333" stroke-width="1.3"><rect x="1" y="1" width="20" height="16" rx="1"/><path d="M8 1v16M14 1v16"/></svg>Columns</div>
</div>

<table class="ex-table">
  <colgroup><col style="width:44px"><col style="width:72px"><col style="width:158px"><col style="width:82px"><col style="width:88px"><col style="width:123px"><col style="width:118px"><col style="width:134px"><col style="width:125px"><col></colgroup>
  <thead><tr><th></th><th></th><th></th><th>Maker Fee</th><th>Taker Fee</th><th>Futures Maker Fee</th><th>Futures Taker Fee</th><th>Trading Fee Discounts</th><th>Discount or Bonus</th><th>Visit</th></tr></thead>
  <tbody>
    <tr><td style="padding-left:20px">☆</td><td>01</td><td><div class="coin"><i style="background:#f7931a"></i>Aurum <span>AUR</span></div></td><td>(eg. 0.10%)</td><td>(eg. 0.20%)</td><td>Fee</td><td>Fee</td><td>(yes/no)</td><td class="bonus">(eg. 10% Off, or<br>$1,000 Bonus)</td><td>www.com</td></tr>
    <tr><td style="padding-left:20px">☆</td><td>02</td><td><div class="coin"><i style="background:#6c6c6c"></i>Ethra <span>ETR</span></div></td><td>(eg. 0.10%)</td><td>(eg. 0.20%)</td><td>Fee</td><td>Fee</td><td>(yes/no)</td><td class="bonus">(eg. 10% Off, or<br>$1,000 Bonus)</td><td>www.com</td></tr>
    <tr><td style="padding-left:20px">☆</td><td>03</td><td><div class="coin"><i style="background:#23292f"></i>Xylo <span>XYL</span></div></td><td>(eg. 0.10%)</td><td>(eg. 0.20%)</td><td>Fee</td><td>Fee</td><td>(yes/no)</td><td class="bonus">(eg. 10% Off, or<br>$1,000 Bonus)</td><td>www.com</td></tr>
    <tr><td style="padding-left:20px">☆</td><td>04</td><td><div class="coin"><i style="background:#26a17b"></i>Anchora <span>ANC</span></div></td><td>(eg. 0.10%)</td><td>(eg. 0.20%)</td><td>Fee</td><td>Fee</td><td>(yes/no)</td><td class="bonus">(eg. 10% Off, or<br>$1,000 Bonus)</td><td>www.com</td></tr>
    <tr><td style="padding-left:20px">☆</td><td>05</td><td><div class="coin"><i style="background:#f3ba2f"></i>Bolt <span>BLT</span></div></td><td>(eg. 0.10%)</td><td>(eg. 0.20%)</td><td>Fee</td><td>Fee</td><td>(yes/no)</td><td class="bonus">(eg. 10% Off, or<br>$1,000 Bonus)</td><td>www.com</td></tr>
    <tr><td style="padding-left:20px">☆</td><td>06</td><td><div class="coin"><i style="background:#1b1b2b"></i>Solvane <span>SVN</span></div></td><td>(eg. 0.10%)</td><td>(eg. 0.20%)</td><td>Fee</td><td>Fee</td><td>(yes/no)</td><td class="bonus">(eg. 10% Off, or<br>$1,000 Bonus)</td><td>www.com</td></tr>
    <tr><td style="padding-left:20px">☆</td><td>07</td><td><div class="coin"><i style="background:#2775ca"></i>Clearcoin <span>CLC</span></div></td><td>(eg. 0.10%)</td><td>(eg. 0.20%)</td><td>Fee</td><td>Fee</td><td>(yes/no)</td><td class="bonus">(eg. 10% Off, or<br>$1,000 Bonus)</td><td>www.com</td></tr>
  </tbody>
</table>

<div class="chart-title" style="left:313px">Maker Fees &nbsp;&nbsp;&nbsp;›</div>
<div class="chart-title" style="left:725px">Trading Volume &nbsp;&nbsp;&nbsp;›</div>

<div class="chart-card" style="left:173px">
  <svg width="418" height="296" viewBox="0 0 418 296">
    <g stroke="#ddd" stroke-width="1"><rect x="56" y="16" width="316" height="266" fill="none"/><path d="M56 52h316M56 97h316M56 142h316M56 187h316M56 232h316"/></g>
    <g fill="#bbb" font-size="13" font-family="Poppins,sans-serif"><text x="33" y="57">50</text><text x="33" y="102">40</text><text x="33" y="147">30</text><text x="33" y="192">20</text><text x="33" y="237">10</text></g>
    <g stroke-linecap="round" stroke-width="7">
      <path d="M90 282V122" stroke="#00AB8E"/><path d="M106 282V70" stroke="#00AB8E"/><path d="M122 282V56" stroke="#00AB8E"/><path d="M137 282V100" stroke="#00AB8E"/><path d="M153 282V83" stroke="#00AB8E"/>
      <path d="M185 282V145" stroke="#00BBA5"/><path d="M201 282V75" stroke="#00BBA5"/><path d="M217 282V135" stroke="#00AB8E"/><path d="M232 282V100" stroke="#00AB8E"/><path d="M248 282V40" stroke="#00AB8E"/>
      <path d="M275 282V110" stroke="#67D7C9"/><path d="M290 282V80" stroke="#67D7C9"/><path d="M306 282V40" stroke="#67D7C9"/><path d="M321 282V100" stroke="#67D7C9"/><path d="M337 282V70" stroke="#67D7C9"/>
    </g>
    <g stroke-width="7" stroke-linecap="round" opacity=".55"><path d="M185 282V240" stroke="#67D7C9"/><path d="M201 282V230" stroke="#67D7C9"/><path d="M217 282V230" stroke="#67D7C9"/><path d="M232 282V235" stroke="#67D7C9"/><path d="M248 282V150" stroke="#C6EFE9"/><path d="M275 282V180" stroke="#C6EFE9"/><path d="M290 282V150" stroke="#C6EFE9"/><path d="M306 282V150" stroke="#C6EFE9"/><path d="M321 282V150" stroke="#C6EFE9"/><path d="M337 282V150" stroke="#C6EFE9"/></g>
  </svg>
</div>

<div class="chart-card" style="left:610px">
  <svg width="418" height="296" viewBox="0 0 418 296">
    <g stroke="#ddd" stroke-width="1" fill="none"><rect x="32" y="21" width="357" height="233"/><path d="M121 21v233M211 21v233M300 21v233M32 44h357M32 67h357M32 90h357M32 113h357M32 136h357M32 159h357M32 182h357M32 205h357M32 228h357"/></g>
    <g fill="#ccc"><circle cx="32" cy="44" r="4"/><circle cx="32" cy="67" r="4"/><circle cx="32" cy="90" r="4"/><circle cx="32" cy="113" r="4"/><circle cx="32" cy="136" r="4"/><circle cx="32" cy="159" r="4"/><circle cx="32" cy="182" r="4"/><circle cx="32" cy="205" r="4"/><circle cx="32" cy="228" r="4"/><circle cx="32" cy="254" r="4"/></g>
    <g fill="none" stroke-width="3">
      <path d="M32 187L83 110L216 168L237 77L388 65" stroke="#00AB8E"/>
      <path d="M32 238L83 137L173 233L226 180L388 95" stroke="#00BBA5"/>
      <path d="M32 200L98 163L253 207L389 146" stroke="#67D7C9"/>
    </g>
    <g fill="#bbb" font-size="16" font-family="Poppins,sans-serif"><text x="56" y="275">2012</text><text x="143" y="275">2013</text><text x="233" y="275">2014</text><text x="323" y="275">2015</text></g>
  </svg>
</div>

<div class="stat" style="left:175px;width:160px"><div class="label">Exchanges Tracked</div><div class="value">125</div></div>
<div class="stat-divider" style="left:368px"></div>
<div class="stat" style="left:405px;width:170px"><div class="label">Average Trading Fee</div><div class="value">0.15%</div></div>
<div class="stat-divider" style="left:607px"></div>
<div class="stat" style="left:640px;width:155px"><div class="label">Total Users</div><div class="value">892M</div></div>
<div class="stat-divider" style="left:831px"></div>
<div class="stat" style="left:865px;width:160px"><div class="label">Web Vistors (30D)</div><div class="value">12.2B</div></div>

<h2 class="section-title" style="top:2009px;font-size:27px">Compare</h2>
<div class="select" style="left:746px">Veltrix &nbsp;⌄</div>
<div class="select" style="left:915px">Harborcoin &nbsp;⌄</div>

<svg class="abs" style="left:60px;top:2080px" width="500" height="300" viewBox="0 0 500 300">
  <g font-family="Poppins,sans-serif" font-size="13" font-weight="500" fill="#111">
    <text x="237" y="29" text-anchor="middle">Fees</text>
    <text x="387" y="116">Features</text>
    <text x="387" y="238">Withdrawals</text>
    <text x="27" y="238">Deposits</text>
    <text x="30" y="116">Security</text>
  </g>
  <g fill="none" stroke="#3d63c9" stroke-width="1">
    <polygon points="237,58 332,113 332,223 237,278 142,223 142,113"/>
    <polygon points="237,74 318,121 318,215 237,262 156,215 156,121"/>
    <polygon points="237,90 304,129 304,207 237,246 170,207 170,129"/>
    <polygon points="237,106 290,137 290,199 237,230 184,199 184,137"/>
    <polygon points="237,122 276,145 276,191 237,214 198,191 198,145"/>
    <polygon points="237,138 262,153 262,183 237,198 212,183 212,153"/>
    <path d="M237 58V278M142 113L332 223M332 113L142 223"/>
  </g>
  <polygon points="237,62 322,120 327,219 237,270 150,220 153,115" fill="none" stroke="#ffe24d" stroke-width="1.2"/>
  <polygon points="237,68 312,124 316,210 237,276 155,212 145,112" fill="none" stroke="#e53935" stroke-width="1.2"/>
</svg>

<div class="score-table">
  <div class="score-head"><span style="width:148px"></span><span style="width:110px">Veltrix</span><span>Harborcoin</span></div>
  <div class="score-row"><span style="width:148px;padding-left:8px">Fees</span><span style="width:122px">9/10</span><span>4/10</span></div>
  <div class="score-row"><span style="width:148px;padding-left:8px">Security</span><span style="width:122px">9/10</span><span>4/10</span></div>
  <div class="score-row"><span style="width:148px;padding-left:8px">Features</span><span style="width:122px">9/10</span><span>4/10</span></div>
  <div class="score-row"><span style="width:148px;padding-left:8px">Deposits</span><span style="width:119px">9/10</span><span>4/10</span></div>
  <div class="score-row"><span style="width:148px;padding-left:8px">Withdrawals</span><span style="width:122px">9/10</span><span>4/10</span></div>
</div>

<div class="panel features">
  <h3>Features</h3><div class="toggle">−</div>
  <div class="feat-list">
    <div class="feat-row"><span class="k"># of Coins</span><span class="a"><b class="up">▲</b>123%</span><span class="b"><b class="down">▼</b>100%</span></div>
    <div class="feat-row"><span class="k"># of Futures</span><span class="a"><b class="up">▲</b>04%</span><span class="b"><b class="down">▼</b>02%</span></div>
    <div class="feat-row"><span class="k">Trading Bots</span><span class="a"><b class="up">▲</b>12345</span><span class="b"><b class="down">▼</b>-</span></div>
    <div class="feat-row"><span class="k">Copy Trading</span><span class="a"><b class="up">▲</b>123456</span><span class="b"><b class="down">▼</b>-</span></div>
    <div class="feat-row"><span class="k">24/7 Support</span><span class="a"><b class="up">▲</b>12345</span><span class="b"><b class="down">▼</b>&nbsp;1245</span></div>
  </div>
</div>
<div class="panel acc" style="top:2364px"><h3>Security</h3><span>+</span></div>
<div class="panel acc" style="top:2429px"><h3>FEES</h3><span>+</span></div>
<div class="panel acc" style="top:2494px"><h3>DEPOSITS</h3><span>+</span></div>
<div class="panel acc" style="top:2559px"><h3>WITHDRAWALS</h3><span>+</span></div>
<div class="btn-full">Full Comparison</div>

<h2 class="section-title" style="top:2762px;font-size:25px;left:-1px">FAQ</h2>
<div class="faq">
  <div class="faq-item">How is this data tracked?<span>⌄</span></div>
  <div class="faq-item">How often is this page updated?<span>⌄</span></div>
  <div class="faq-item open">What Are Crypto Exchanges?<span>⌄</span></div>
  <div class="faq-item">How To Choose a Crypto Exchange?<span>⌄</span></div>
</div>

<section class="newsletter">
  <h2>Interested to stay up-to-date with cryptocurrencies?</h2>
  <p>Get the latest crypto news, updates, and reports by subscribing to our free newsletter.</p>
  <div class="email">Enter your email address</div>
  <div class="subscribe">Subscribe</div>
</section>

<footer class="footer">
  <p class="copy">© 2025 crypto exchange . All Rights Reserved.</p>
  <p>crypto exchange: All content provided herein our website, hyperlinked sites, associated applications, forums, blogs, social media accounts and other platforms (“Site”) is for your general information only, procured from third party sources. We make no warranties of any kind in relation to our content, including but not limited to accuracy and updatedness. No part of the content that we provide constitutes financial advice, legal advice or any other form of advice meant for your specific reliance for any purpose. Any use or reliance on our content is solely at your own risk and discretion. You should conduct your own research, review, analyse and verify our content before relying on them. Trading is a highly risky activity that can lead to major losses, please therefore consult your financial advisor before making any decision. No content on our Site is meant to be a solicitation or offer.</p>
</footer>

</body>
</html>
```